continuing medical education travel company. luxury, professional, quality service

PLEASE USE THE REVISED LOGO FOR ALL CARD DESIGNS, NO SNAKE HEAD

Target Market(s)

physicians

Industry/Entity Type

Travel Industry

Contact Information for Business Card

luxury quality, spot uv, foil, rounded corners

Colors
0255a3
3176b5
cfdeed
aaaaaa
5c5c5c

Requirements
Must have
• navy, platinum, possible holographic

```html
<!DOCTYPE html>
<html lang="en">
<head>
<meta charset="utf-8">
<title>Calder Travel — Business Card</title>
<link rel="stylesheet" href="https://fonts.googleapis.com/css2?family=Tinos:wght@400;700&display=swap">
<style>
  :root {
    --backdrop: #e6e6e8;
    --navy-deep: #1f237a;
    --navy-glow: #4a4fb0;
    --platinum-light: #dcdcdc;
    --platinum: #aaaaaa;
    --platinum-dark: #8c8c8c;
    --ink: #111111;
    --ink-soft: #2a2a2a;
    --white: #ffffff;
    --accent-blue: #0255a3;
    --accent-navy: #2b2f86;
  }
  * { box-sizing: border-box; margin: 0; padding: 0; }
  html, body {
    width: 1200px; height: 900px; overflow: hidden;
    background: var(--backdrop);
    font-family: "Tinos", "Times New Roman", serif;
  }
  .canvas { position: relative; width: 1200px; height: 900px; }

  .card {
    position: absolute;
    width: 560px; height: 320px;
    border-radius: 14px;
    box-shadow: 0 10px 26px rgba(0,0,0,.22);
    overflow: hidden;
  }

  /* Front */
  .card--front {
    left: 80px; top: 100px;
    background: radial-gradient(ellipse 55% 60% at 45% 45%, var(--navy-glow), var(--navy-deep) 80%);
    display: flex; align-items: center; justify-content: center;
  }
  .wordmark {
    color: var(--white);
    font-weight: 400;
    text-align: center;
    line-height: 1;
  }
  .wordmark__name { display: block; font-size: 74px; letter-spacing: 2px; }
  .wordmark__sub { display: block; font-size: 24px; letter-spacing: 22px; margin-top: 8px; padding-left: 22px; }

  /* Back */
  .card--back {
    left: 560px; top: 490px;
    background: radial-gradient(ellipse 60% 70% at 55% 40%, var(--platinum-light), var(--platinum) 55%, var(--platinum-dark));
  }
  .card--back .wordmark {
    position: absolute; left: 40px; top: 78px;
  }
  .card--back .wordmark__name { font-size: 58px; }
  .card--back .wordmark__sub { font-size: 19px; letter-spacing: 17px; padding-left: 17px; }

  .divider {
    position: absolute; left: 318px; top: 40px;
    width: 2px; height: 190px;
    background: linear-gradient(to bottom, rgba(255,255,255,.9), var(--accent-navy));
  }

  .contact { position: absolute; left: 338px; top: 70px; color: var(--ink); }
  .contact__name { font-size: 25px; font-weight: 700; }
  .contact__role { font-size: 15px; color: var(--ink-soft); margin: 2px 0 12px; }
  .contact__list { list-style: none; }
  .contact__item {
    display: flex; align-items: center; gap: 8px;
    font-size: 16px; line-height: 24px;
  }
  .contact__icon { width: 14px; height: 14px; flex: none; }

  .address {
    position: absolute; left: 120px; bottom: 44px;
    font-size: 17px; color: var(--ink-soft);
  }
</style>
</head>
<body>
<main class="canvas">

  <section class="card card--front" aria-label="Card front">
    <div class="wordmark">
      <span class="wordmark__name">CALDER</span>
      <span class="wordmark__sub">TRAVEL</span>
    </div>
  </section>

  <section class="card card--back" aria-label="Card back">
    <div class="wordmark">
      <span class="wordmark__name">CALDER</span>
      <span class="wordmark__sub">TRAVEL</span>
    </div>

    <div class="divider"></div>

    <div class="contact">
      <p class="contact__name">Daniel Hart</p>
      <p class="contact__role">Managing director</p>
      <ul class="contact__list">
        <li class="contact__item">
          <svg class="contact__icon" viewBox="0 0 14 14" aria-hidden="true">
            <rect width="14" height="14" rx="2" fill="var(--accent-navy)"/>
            <path d="M4 3.5c-.6.6-.6 2 .8 3.8s3.2 2.8 4 2.2l.8-.8-1.6-1.4-.8.6c-.8-.4-1.6-1.2-2-2l.6-.8L4.8 3z" fill="var(--white)"/>
          </svg>
          +(000) 5550 1428
        </li>
        <li class="contact__item">
          <svg class="contact__icon" viewBox="0 0 14 14" aria-hidden="true">
            <rect width="14" height="14" rx="2" fill="var(--accent-navy)"/>
            <rect x="3" y="4.5" width="8" height="5.5" fill="none" stroke="var(--white)" stroke-width="1"/>
            <path d="M3 4.5l4 3 4-3" fill="none" stroke="var(--white)" stroke-width="1"/>
          </svg>
          daniel@caldertravel.com
        </li>
        <li class="contact__item">
          <svg class="contact__icon" viewBox="0 0 14 14" aria-hidden="true">
            <rect width="14" height="14" rx="2" fill="var(--accent-navy)"/>
            <circle cx="7" cy="7" r="3.6" fill="none" stroke="var(--white)" stroke-width="1"/>
            <path d="M3.4 7h7.2M7 3.4c-1.6 2-1.6 5.2 0 7.2M7 3.4c1.6 2 1.6 5.2 0 7.2" fill="none" stroke="var(--white)" stroke-width=".8"/>
          </svg>
          www.caldertravel.com
        </li>
      </ul>
    </div>

    <p class="address">418 Harbor Lane, Boston 02110</p>
  </section>

</main>
</body>
</html>
```